Web Site for Strategy and Technology Consulting Company

We are looking for a website design that engages potential customers to understand our services and contact us. In this contest, we are looking for a homepage design, but the winning designer will be favored for the design of some of the more complicated interior pages of the site. An additional contest (or contests) for these pages will be added soon.

PLATROM AND RESPONSIVE DESIGN
The site will be implemented in WordPress using the Elementor page builder.
We are looking for a design that will look good on phones are well as laptop browsers.

UPLOADED FILES INCLUDE:
1a A wireframe of the homepage we are looking for. The Uploaded PDF also includes a draft of the text proposed for the homepage. Designers are free to go beyond the wireframe, but all elements of the wireframe should be included.
1b A Word document with the draft text of the homepage.
2a-d The Norvalith logo. Two versions are included – a dark version which works well against a light background, and a light version which works well against a dark background.
3 The Norvalith color palette with HEX and RGB values. Designers are not limited to this palette, but colors should be complementary.
4 A draft of the homepage menu
5 Service sheets with information on the services we provide

MORE ABOUT NORVALITH
Norvalith is a consulting company focused on transforming businesses through software. Our tagline, “Transformation Delivered,” recognizes the gap business often have between business transformation and the software they end up with. By listening to our customers and understanding their vision and where they are, we help get our customers where they want to go.

We increase our capability by working with many consultants and partners, allowing us to provide our customers with the best people and the software that best suits them.

Industry/Entity Type

Consulting

Number of Pages Required

1 page

Font styles to use
Sans Serif

Requirements
Must have
• the content represented on the wireframe uploaded
Nice to have
• interactive features, such as roll-over icons that reveal additional information

```html
<!DOCTYPE html>
<html lang="en">
<head>
<meta charset="utf-8">
<title>Norvalith – Homepage Presentation</title>
<link href="https://fonts.googleapis.com/css2?family=Poppins:wght@300;400;500;600;700&display=swap" rel="stylesheet">
<style>
:root{
  --blue:#245d95;
  --blue-text:#1f5c93;
  --navy:#12133f;
  --ink:#16161f;
  --gold:#e2b513;
  --gold-band:#bba33a;
  --pale:#f1f5fa;
  --ring:#c9d8e6;
  --grey:#8d8f98;
  --white:#fff;
}
*{margin:0;padding:0;box-sizing:border-box}
html,body{width:1200px;height:1200px;overflow:hidden;background:var(--white);font-family:'Poppins',sans-serif;color:var(--ink)}
.board{position:absolute;left:0;top:0;width:1932px;height:1932px;transform:scale(.62112);transform-origin:0 0;overflow:hidden;background:var(--white)}
.abs{position:absolute}
.backdrop{position:absolute;inset:0}
.page{position:absolute;background:var(--white);overflow:hidden}
.page-right{left:1070px;top:0;width:690px;height:1932px;box-shadow:0 0 40px rgba(0,0,0,.08)}
.page-left{left:177px;top:261px;width:956px;height:1671px;box-shadow:0 0 50px rgba(0,0,0,.15);z-index:2}
.btn{position:absolute;background:var(--gold);color:var(--white);font-weight:600;display:flex;align-items:center;justify-content:center;box-shadow:0 4px 8px rgba(226,181,19,.3);border-radius:2px}
.h-blue{color:var(--blue-text);font-weight:600}
.h-dark{color:var(--ink);font-weight:600}
.body-text{color:var(--grey);font-weight:300}
.photo{position:absolute}
.topbar{position:absolute;left:0;top:0;width:956px;height:25px;background:var(--blue);color:var(--white);font-size:8px}
.topbar span{position:absolute;top:8px;display:flex;align-items:center;gap:6px}
.ico-c{width:12px;height:12px;border:1px solid rgba(255,255,255,.8);border-radius:50%;display:inline-block}
.nav{position:absolute;left:0;top:25px;width:956px;height:60px;background:var(--white);box-shadow:0 2px 8px rgba(0,0,0,.05)}
.brand{position:absolute;font-weight:400;color:#3a3b44;display:flex;align-items:center;gap:6px}
.brand i{display:inline-block;background:var(--blue)}
.nav-link{position:absolute;top:26px;font-size:9px;color:#333}
.section-pale{position:absolute;background:var(--pale)}
.card{position:absolute;background:var(--white);box-shadow:0 2px 12px rgba(0,0,0,.05);border-radius:3px}
.card.active{background:var(--gold)}
.card h4{position:absolute;color:var(--blue-text);font-weight:500}
.card p{position:absolute;color:var(--grey);font-weight:300}
.card.active h4,.card.active p{color:var(--white)}
.card svg{position:absolute}
.t-card{position:absolute;top:1304px;width:180px;height:118px;background:var(--white);box-shadow:0 2px 12px rgba(0,0,0,.05)}
.t-card .av{position:absolute;left:8px;top:18px;width:30px;height:30px;border-radius:50%}
.t-card .nm{position:absolute;left:50px;top:20px;font-size:9px;color:#2c3a7a}
.t-card .rl{position:absolute;left:50px;top:32px;font-size:6px;color:var(--grey)}
.t-card .st{position:absolute;left:50px;top:40px;font-size:9px;color:#2c3a7a;letter-spacing:2px}
.t-card .q{position:absolute;right:12px;top:18px;font-size:14px;color:var(--gold);font-weight:600}
.t-card p{position:absolute;left:8px;top:70px;width:150px;font-size:6px;line-height:11px;color:var(--grey)}
.partners{position:absolute;left:95px;top:1592px;width:500px;height:40px;display:flex;align-items:center;justify-content:space-between}
.partner{font-weight:600;font-size:19px;color:var(--blue);white-space:nowrap;line-height:1}
.partner.small{font-size:11px}
.footer{position:absolute;left:0;top:1680px;width:690px;height:252px;background:var(--navy);color:var(--white)}
.footer h5{position:absolute;top:72px;font-size:9px;font-weight:500}
.footer ul{position:absolute;top:98px;list-style:none;font-size:6px;line-height:14px;color:#c9cbe0}
.soc{position:absolute;width:14px;height:14px;border:1px solid rgba(255,255,255,.8);border-radius:50%}
.dots{position:absolute;background-image:radial-gradient(#c8cbd6 1.5px,transparent 1.6px);background-size:12px 12px}
.tick{display:inline-block;width:9px;height:9px;border-radius:50%;background:var(--gold);margin-right:6px;vertical-align:middle}
</style>
</head>
<body>
<div class="board">
  <svg class="backdrop" width="1932" height="1932" viewBox="0 0 1932 1932" aria-hidden="true">
    <circle cx="60" cy="130" r="300" fill="none" stroke="var(--ring)" stroke-width="120"/>
    <path d="M1700 1440 Q1850 1440 1932 1500 L1932 1470 Q1850 1410 1700 1410Z" fill="#dfe7f0"/>
    <path d="M0 1525 Q900 1420 1932 1480 L1932 1932 L0 1932Z" fill="var(--gold-band)"/>
  </svg>

  <section class="page page-right">
    <div class="photo" role="img" aria-label="Collage of consultants with a digital finance interface" style="left:95px;top:0;width:238px;height:210px;background:linear-gradient(135deg,#2f6d9c,#1b3d63 60%,#d9dde3)"></div>
    <div class="abs" style="left:244px;top:178px;font-size:8px;color:#333">Years of experience</div>
    <div class="abs h-blue" style="left:382px;top:6px;font-size:22px;line-height:26px">Transformation<br><span style="color:var(--ink)">Delivered</span></div>
    <p class="abs body-text" style="left:382px;top:70px;width:210px;font-size:6px;line-height:11px">We do more for our customers than implement software. We listen. We work to understand where they are in their transformation journey and where they want to go. We partner with them to clear the roadblocks that stand in their way, ensuring they reach their destination</p>
    <div class="btn" style="left:382px;top:152px;width:70px;height:20px;font-size:6px">Read More</div>

    <div class="section-pale" style="left:0;top:265px;width:690px;height:360px"></div>
    <div class="abs h-dark" style="left:60px;top:315px;font-size:22px;line-height:27px">Transformation Supported<br>By Technology</div>
    <div class="btn" style="left:527px;top:350px;width:103px;height:20px;font-size:6px">How We Work Button</div>
    <div class="card" style="left:58px;top:410px;width:134px;height:145px"><svg width="34" height="30" style="left:12px;top:14px"><use href="#svc-icon"/></svg><h4 style="left:12px;top:56px;font-size:8px">Transformation Planning</h4><p style="left:12px;top:80px;width:110px;font-size:6px;line-height:11px">Lorem Ipsum is simply dummy text of the printing and typesetting industry.</p></div>
    <div class="card" style="left:204px;top:410px;width:134px;height:145px"><svg width="34" height="30" style="left:12px;top:14px"><use href="#svc-icon"/></svg><h4 style="left:12px;top:56px;font-size:8px">CRM Solutions</h4><p style="left:12px;top:80px;width:110px;font-size:6px;line-height:11px">Lorem Ipsum is simply dummy text of the printing and typesetting industry.</p></div>
    <div class="card active" style="left:350px;top:410px;width:134px;height:145px"><svg width="34" height="30" style="left:12px;top:14px;color:#fff"><use href="#svc-icon"/></svg><h4 style="left:12px;top:56px;font-size:8px">ERP Solutions</h4><p style="left:12px;top:80px;width:110px;font-size:6px;line-height:11px">Lorem Ipsum is simply dummy text of the printing and typesetting industry.</p></div>
    <div class="card" style="left:496px;top:410px;width:134px;height:145px"><svg width="34" height="30" style="left:12px;top:14px"><use href="#svc-icon"/></svg><h4 style="left:12px;top:56px;font-size:8px;line-height:13px">Data And Business<br>Intelligence</h4><p style="left:12px;top:92px;width:110px;font-size:6px;line-height:11px">Lorem Ipsum is simply dummy text of the printing and typesetting industry.</p></div>
    <div class="card" style="left:642px;top:410px;width:134px;height:145px"><svg width="34" height="30" style="left:12px;top:14px"><use href="#svc-icon"/></svg><h4 style="left:12px;top:56px;font-size:8px">Amplify</h4><p style="left:12px;top:80px;width:110px;font-size:6px;line-height:11px">Lorem Ipsum is simply dummy text of the printing and typesetting industry.</p></div>

    <div class="abs h-dark" style="left:0;width:690px;text-align:center;top:678px;font-size:24px">Resources</div>
    <p class="abs body-text" style="left:260px;width:170px;text-align:center;top:716px;font-size:6px;line-height:11px">Lorem Ipsum is simply dummy text of the printing and typesetting industry.</p>
    <div class="dots" style="left:78px;top:790px;width:36px;height:96px"></div>
    <div class="abs" style="left:107px;top:768px;width:238px;height:14px;background:#e9ebef"></div>
    <div class="photo" role="img" aria-label="Overhead view of a team working at laptops with sticky notes" style="left:118px;top:780px;width:227px;height:267px;background:linear-gradient(160deg,#d4d6da,#8f949c 50%,#e3e4e6)"></div>
    <div class="abs h-blue" style="left:389px;top:790px;font-size:22px;line-height:27px">Transformation<br><span style="color:var(--ink)">Delivered</span></div>
    <p class="abs body-text" style="left:389px;top:855px;width:215px;font-size:6px;line-height:11px">The world has changed in the past twenty years. The people you need might not all work for one company. Our clients want the best resources, available quickly. That's why, in addition to our team of experts, we partner with:</p>
    <p class="abs" style="left:389px;top:914px;width:215px;font-size:6px;line-height:11px;color:#444"><span class="tick"></span>A large network of expert consultants who are the best at what they do</p>
    <p class="abs" style="left:389px;top:944px;width:215px;font-size:6px;line-height:11px;color:#444"><span class="tick"></span>Service providers all over the world to provide the resources and value that are right for you, available 24 x 7.</p>
    <p class="abs body-text" style="left:389px;top:980px;width:215px;font-size:6px;line-height:11px">People are invariably at the center of our customer's success. Find out how we can add our experts to yours.</p>
    <div class="btn" style="left:303px;top:1088px;width:84px;height:20px;font-size:6px">Meet Our Team</div>

    <div class="section-pale" style="left:0;top:1170px;width:690px;height:330px"></div>
    <div class="abs h-blue" style="left:0;width:666px;text-align:center;top:1210px;font-size:22px">Testimonials</div>
    <p class="abs body-text" style="left:250px;width:170px;text-align:center;top:1249px;font-size:6px;line-height:11px">Lorem ipsum dolor sit amet, consetetur sadipscing elitr, sed diam nonumy</p>
    <div class="t-card" style="left:63px;width:172px"><div class="av" role="img" aria-label="Client portrait" style="background:#c9a28a"></div><div class="nm">Marla Finch</div><div class="rl">Ceo and founder</div><div class="st">★★★★</div><div class="q">❞</div><p>Lorem ipsum dolor sit amet, consetetur sadipscing elitr, sed diam nonumy eirmod lorem ipsum dolor sit</p></div>
    <div class="t-card" style="left:251px;width:189px"><div class="av" role="img" aria-label="Client portrait" style="background:#3a2a24"></div><div class="nm">Theo Brandt</div><div class="rl">Ceo and founder</div><div class="st">★★★★★</div><div class="q">❞</div><p>Lorem ipsum dolor sit amet, consetetur sadipscing elitr, sed diam nonumy eirmod lorem ipsum dolor sit</p></div>
    <div class="t-card" style="left:456px;width:189px"><div class="av" role="img" aria-label="Client portrait" style="background:#5f7f92"></div><div class="nm">Ines Walcott</div><div class="rl">Ceo and founder</div><div class="st">★★★★★</div><div class="q">❞</div><p>Lorem ipsum dolor sit amet, consetetur sadipscing elitr, sed diam nonumy eirmod lorem ipsum dolor sit</p></div>
    <svg class="abs" style="left:312px;top:1451px" width="44" height="6"><rect x="0" y="1" width="6" height="3" fill="#d6dbe4"/><rect x="9" y="1" width="6" height="3" fill="#d6dbe4"/><rect x="18" y="1" width="8" height="3" fill="var(--gold)"/><rect x="29" y="1" width="6" height="3" fill="#d6dbe4"/><rect x="38" y="1" width="6" height="3" fill="#d6dbe4"/></svg>

    <div class="abs h-blue" style="left:0;width:690px;text-align:center;top:1537px;font-size:22px">Technologies</div>
    <div class="partners">
      <span class="partner">Corvane</span>
      <span class="partner small">Tellix</span>
      <span class="partner">Shorea</span>
      <span class="partner">Rovik</span>
      <span class="partner">Belmora</span>
    </div>

    <footer class="footer">
      <div class="brand" style="left:62px;top:62px;font-size:26px;color:#fff"><i style="width:8px;height:8px;background:#fff"></i>Norvalith</div>
      <p class="abs" style="left:62px;top:100px;width:150px;font-size:6px;line-height:11px;color:#c9cbe0">Lorem ipsum dolor sit amet, consetetur sadipscing elitr, sed diam nonumy eirmod lorem ipsum dolor sit amet, consetetur sadipscing elitr, sed diam</p>
      <div class="soc" style="left:62px;top:162px"></div><div class="soc" style="left:84px;top:162px"></div><div class="soc" style="left:106px;top:162px"></div>
      <h5 style="left:273px">Quick Links</h5>
      <ul style="left:273px"><li>Home</li><li>About us</li><li>Services</li><li>Join Us</li><li>Contact us</li></ul>
      <h5 style="left:407px">Services</h5>
      <ul style="left:407px"><li>Transformation Planning</li><li>CRM Solutions</li><li>ERP Solutions</li><li>Data And Business Intelligence</li><li>Amplify</li></ul>
      <h5 style="left:547px">Get In Touch</h5>
      <ul style="left:547px"><li>◯ Call: +414-555-0142</li><li>◯ Fax: +414-555-0187</li><li>◯ Email: info@norvalith-mail.com</li></ul>
      <div class="abs" style="left:62px;top:222px;font-size:6px;color:#c9cbe0">© 2002-2015 Norvalith All rights reserved</div>
      <div class="abs" style="left:460px;top:222px;font-size:6px;color:#c9cbe0">Site map &nbsp;|&nbsp; Terms and conditions &nbsp;|&nbsp; Privacy Policy</div>
    </footer>
  </section>

  <section class="page page-left">
    <div class="topbar">
      <span style="left:78px"><i class="ico-c"></i>Call: +414-555-0142</span>
      <span style="left:238px"><i class="ico-c"></i>Fax: +414-555-0187</span>
      <span style="left:398px"><i class="ico-c"></i>Login/Signup</span>
      <span style="left:830px;top:6px;gap:4px"><i class="ico-c"></i><i class="ico-c"></i><i class="ico-c"></i></span>
    </div>
    <nav class="nav">
      <div class="brand" style="left:78px;top:10px;font-size:36px"><i style="width:9px;height:9px"></i>Norvalith</div>
      <span class="nav-link" style="left:478px;color:var(--blue-text)">Home</span>
      <span class="nav-link" style="left:527px">About Us</span>
      <span class="nav-link" style="left:592px">Services</span>
      <span class="nav-link" style="left:654px">Insights</span>
      <span class="nav-link" style="left:715px">Join Us</span>
      <div class="btn" style="left:792px;top:16px;width:85px;height:29px;font-size:9px">Contact</div>
    </nav>
    <div class="photo" role="img" aria-label="Two consultants in discussion, one giving a thumbs up, in a bright office" style="left:0;top:85px;width:956px;height:507px;background:linear-gradient(90deg,#fff 0%,#f4f6f8 30%,#b9c3cf 52%,#3b5576 65%,#b58d67 82%,#dfe4ea 100%)"></div>
    <div class="abs" style="left:78px;top:234px;font-size:17px;color:var(--blue-text);font-weight:500;letter-spacing:2.5px">Welcome To</div>
    <div class="abs" style="left:76px;top:260px;font-size:52px;font-weight:700;letter-spacing:1px">NORVALITH</div>
    <div class="abs" style="left:78px;top:338px;font-size:12px;color:var(--grey);letter-spacing:1px;font-weight:300">Strategy and Technology Consulting Company</div>
    <div class="btn" style="left:78px;top:387px;width:91px;height:30px;font-size:9px">Our Story</div>

    <div class="abs" style="left:184px;top:679px;width:264px;height:150px;background:var(--gold)"></div>
    <div class="dots" style="left:150px;top:702px;width:36px;height:118px"></div>
    <div class="abs" style="left:133px;top:842px;width:70px;height:10px;background:var(--blue)"></div>
    <div class="photo" role="img" aria-label="Consultant holding a tablet in front of a digital finance display" style="left:197px;top:692px;width:264px;height:312px;background:linear-gradient(135deg,#2f6d9c,#1d4670 55%,#8fb6cf)"></div>
    <div class="photo" role="img" aria-label="Two colleagues reviewing work at a computer" style="left:129px;top:852px;width:174px;height:203px;background:linear-gradient(160deg,#e8ecef,#9aa3ad 55%,#dfe3e6);border-bottom:4px solid var(--blue)"></div>
    <div class="dots" style="left:330px;top:1010px;width:70px;height:30px"></div>
    <div class="abs" style="left:300px;top:1014px;font-size:16px;font-weight:600">5</div>
    <div class="abs" style="left:339px;top:1016px;font-size:11px;color:#333;letter-spacing:.5px">Years of experience</div>
    <div class="abs" style="left:529px;top:749px;font-size:10px;letter-spacing:4px;color:#333">ABOUT US</div>
    <div class="abs" style="left:630px;top:753px;width:37px;height:2px;background:#2c3a7a"></div>
    <div class="abs h-blue" style="left:529px;top:772px;font-size:32px;line-height:37px">Transformation<br><span style="color:var(--ink)">Delivered</span></div>
    <p class="abs body-text" style="left:529px;top:862px;width:300px;font-size:9.5px;line-height:15.5px;letter-spacing:.3px">We do more for our customers than implement software. We listen. We work to understand where they are in their transformation journey and where they want to go. We partner with them to clear the roadblocks that stand in their way, ensuring they reach their destination</p>
    <div class="btn" style="left:529px;top:977px;width:97px;height:29px;font-size:9px">Read More</div>

    <div class="section-pale" style="left:0;top:1136px;width:956px;height:535px"></div>
    <svg class="abs" style="left:790px;top:1520px" width="170" height="150" aria-hidden="true"><circle cx="160" cy="150" r="120" fill="none" stroke="#e3e9f2" stroke-width="40"/></svg>
    <div class="abs h-dark" style="left:78px;top:1204px;font-size:32px;line-height:37px;letter-spacing:1px">Transformation Supported<br>By Technology</div>
    <div class="btn" style="left:731px;top:1253px;width:145px;height:29px;font-size:9px">How We Work Button</div>
    <div class="card" style="left:78px;top:1337px;width:187px;height:203px"><svg width="46" height="44" style="left:16px;top:18px"><use href="#svc-icon"/></svg><h4 style="left:16px;top:79px;font-size:11.5px">Transformation Planning</h4><p style="left:16px;top:110px;width:160px;font-size:9px;line-height:15.5px">Lorem Ipsum is simply dummy text of the printing and typesetting industry.</p></div>
    <div class="card" style="left:281px;top:1337px;width:188px;height:203px"><svg width="46" height="44" style="left:16px;top:18px"><use href="#svc-icon"/></svg><h4 style="left:16px;top:79px;font-size:11.5px">CRM Solutions</h4><p style="left:16px;top:110px;width:160px;font-size:9px;line-height:15.5px">Lorem Ipsum is simply dummy text of the printing and typesetting industry.</p></div>
    <div class="card active" style="left:485px;top:1337px;width:187px;height:203px"><svg width="46" height="44" style="left:16px;top:18px;color:#fff"><use href="#svc-icon"/></svg><h4 style="left:16px;top:79px;font-size:11.5px">ERP Solutions</h4><p style="left:16px;top:110px;width:160px;font-size:9px;line-height:15.5px">Lorem Ipsum is simply dummy text of the printing and typesetting industry.</p></div>
    <div class="card" style="left:688px;top:1337px;width:188px;height:203px"><svg width="46" height="44" style="left:16px;top:18px"><use href="#svc-icon"/></svg><h4 style="left:16px;top:79px;font-size:11.5px;line-height:17px">Data And Business<br>Intelligence</h4><p style="left:16px;top:127px;width:160px;font-size:9px;line-height:15.5px">Lorem Ipsum is simply dummy text of the printing and typesetting industry.</p></div>
    <div class="card" style="left:892px;top:1337px;width:188px;height:203px"><svg width="46" height="44" style="left:16px;top:18px"><use href="#svc-icon"/></svg><h4 style="left:16px;top:79px;font-size:11.5px">Amplify</h4><p style="left:16px;top:110px;width:160px;font-size:9px;line-height:15.5px">Lorem Ipsum is simply dummy text of the printing and typesetting industry.</p></div>
  </section>

  <svg width="0" height="0" style="position:absolute" aria-hidden="true">
    <symbol id="svc-icon" viewBox="0 0 46 44">
      <g fill="none" stroke="#2c3a7a" stroke-width="1.6" style="stroke:currentColor">
        <rect x="8" y="8" width="30" height="24" rx="1.5"/>
        <path d="M3 35 H43 L40 39 H6 Z"/>
        <circle cx="23" cy="21" r="4"/>
        <path d="M16 32 Q23 24 30 32"/>
        <rect x="18" y="1" width="10" height="7"/>
        <path d="M22 2.8 V6.2 L25 4.5 Z"/>
      </g>
    </symbol>
  </svg>
</div>
</body>
</html>
```